International Marketing Company - Web Design Project

kVesta is a well-funded start up in London developing an Online Marketing Platform for small businesses in Europe.

We require a large number of high quality business web designs for our business website builder. Our business websites are completely integrated into our Online Marketing systems and therefore it is important for designers to comply with our Design Guidelines.

This initial contest is a trial for us to open up the design process to top designers for the Builders vertical (e.g. Builders, Electricians, Plumbers, Flooring, etc.). We have implemented a base html structure and design and included them in the files.

Use your creativity to design new and fresh designs based on the included elements (e.g. testimonials, business description, etc).

We will award the stated prize money for the top three designs.

Any designers that submit designs we feel are of a high enough quality but do not make the top 3 could still be compensated and WILL be invited to participate in our next vertical competition.

Therefore, we encourage designers to submit as many designs as possible as we may award up to 25 designs.

Submissions will be reviewed daily and feedback provided where possible.

Designers who can also code will have the options to implement their designs for an additional fee.

Good luck!
Updates

There has been a mistake made in regard to the prize. Pixel Harbor should have it fixed soon.

1st place = £350
2nd place = £250
3rd Place = £150

Thanks,
Dorian
25/11/2011

UPDATE:

1st place will win £350
2nd place will win £250
3rd place will win £150

Everything else is as to the specification.

Thanks
Dorian

Target Market(s)

Builders, Electricians, Plumbers, Tradesman, Small construction companies

Industry/Entity Type

Business

Requirements
Must have
• Totally new designs based around the elements we want to show on each page.

We are looking for something different to the design we already have. But you can use that as a starting point.

Use the included files to see what is required for each page. Here is a brief outline:

Homepage - Testimonials, News, Business Description, Latest Projects and Call to action

About-Us - Team Summary, About the Business and a call to action

Projects Page - Project Details (Oage Title and description), Each project needs a title, content and 2 images.

Testimonials Page - The testifiers name and their comment

Contacts Page - Trovix Map, Company address, business hours, contact form and a call to action.

Please submit final designs in Photoshop or Fireworks format.

Each page has a set of elements. These element must feature in the design of that page. See supporting documents for page details.

All elements must be included in your design. Please do not add any extra element.

Professional look and feel
Nice to have
• Design variations:
Full width designs
Boxed Designs
With AND without carousels
OR static images
Good use of stock images.

Creative use of the elements, dont be restricted/influenced by the default design we have already

Designs based on the 960 grid

```html
<!DOCTYPE html>
<html lang="en">
<head>
<meta charset="utf-8">
<title>kVesta – Builders</title>
<link rel="stylesheet" href="https://fonts.googleapis.com/css2?family=Graduate&family=Arimo:ital,wght@0,400;0,700;1,400&display=swap">
<style>
:root{
  --header-top:#2ec4ee;
  --header-bottom:#13a6d8;
  --brand-navy:#0d3a63;
  --brand-blue:#1a6fa0;
  --accent-teal:#1597be;
  --accent-red:#d7261b;
  --cta-yellow:#ffc92e;
  --cta-yellow-dark:#f2ac12;
  --ink:#111;
  --body-text:#1d3f62;
  --muted:#666;
  --page:#dcdcdc;
  --hero-light:#eef3f6;
  --hero-mid:#d3dde3;
  --footer-grey:#c9c9c9;
  --white:#fff;
}
*{box-sizing:border-box;margin:0;padding:0}
html,body{width:1121px;height:1200px;overflow:hidden}
body{position:relative;background:linear-gradient(#e6e6e6,var(--page));font-family:"Arimo",Arial,sans-serif;color:var(--ink)}
.display{font-family:"Graduate",Georgia,serif}

.site-header{position:absolute;left:0;top:0;width:1121px;height:67px;background:linear-gradient(var(--header-top),var(--header-bottom));box-shadow:0 2px 4px rgba(0,0,0,.25)}
.logo{position:absolute;left:128px;top:15px;font-size:30px;color:var(--brand-navy)}
.main-nav{position:absolute;left:406px;top:22px;display:flex;gap:28px}
.main-nav a{font-family:"Graduate",Georgia,serif;font-size:16px;color:var(--white);text-decoration:none;letter-spacing:.3px}

.hero{position:absolute;left:0;top:67px;width:1121px;height:354px;background:radial-gradient(ellipse at 70% 40%,var(--hero-light),var(--hero-mid));border-bottom:1px solid #bfc6ca}
.hero-photo{position:absolute;left:123px;top:21px;width:503px;height:293px;background:var(--white);border-radius:6px;box-shadow:0 1px 5px rgba(0,0,0,.3);padding:10px}
.hero-photo .fill{width:100%;height:100%;background:linear-gradient(120deg,#cfd8e0,#7d8793 45%,#3a3f4a 70%,#b8c2cb)}
.hero-copy{position:absolute;left:650px;top:53px}
.hero-copy .line{font-size:31px;line-height:42px;color:var(--ink)}
.hero-copy .big{font-size:72px;line-height:80px;color:var(--brand-blue);letter-spacing:1px}
.cta{position:absolute;left:648px;top:226px;width:174px;height:44px;background:linear-gradient(var(--cta-yellow),var(--cta-yellow-dark));border-radius:3px;box-shadow:0 2px 3px rgba(0,0,0,.3);font-family:"Graduate",Georgia,serif;font-size:24px;color:var(--ink);text-align:center;line-height:44px}

.section-title{position:absolute;font-size:17px;color:var(--ink)}
.about-text{position:absolute;left:123px;top:498px;width:530px;font-size:12.5px;line-height:16px;color:var(--body-text)}
.more-link{position:absolute;font-family:"Graduate",Georgia,serif;font-size:11px;color:var(--accent-red);text-decoration:none}
.more-link::after{content:" ›";font-family:"Arimo",Arial,sans-serif;font-weight:700;font-size:15px}

.projects{position:absolute;left:123px;top:643px;display:flex;gap:12px}
.project{width:130px}
.project .thumb{height:105px;background:var(--white);padding:6px;border-radius:4px;box-shadow:0 1px 3px rgba(0,0,0,.25)}
.project .thumb div{width:100%;height:100%}
.project p{margin-top:14px;font-size:12px;line-height:15px;color:var(--body-text);padding-left:3px}

.testimonials{position:absolute;left:715px;top:421px;width:280px;height:422px;background:var(--white);border-radius:0 0 6px 6px;box-shadow:0 2px 6px rgba(0,0,0,.25);padding:45px 24px 0 26px}
.testimonials h2{font-size:16px;line-height:20px;color:var(--ink);margin-bottom:18px}
.testimonial{border-bottom:1px solid #ddd;margin-bottom:12px}
.testimonial h3{font-size:16px;color:var(--brand-blue);font-weight:700;padding-bottom:6px;border-bottom:1px solid #e3e3e3;margin-bottom:8px}
.testimonial p{font-size:12.5px;line-height:16px;font-style:italic;color:var(--body-text);padding-bottom:2px}
.testimonial:last-of-type{border-bottom:none}

.news-bar{position:absolute;left:123px;top:875px;width:874px;height:45px;background:#c7c7c7;border-radius:4px}
.news-label{position:absolute;left:0;top:0;height:45px;width:170px;background:var(--accent-teal);border-radius:4px 0 0 4px;color:var(--white);font-size:17px;line-height:45px;padding-left:24px}
.news-label svg{position:absolute;right:-12px;top:0}
.news-text{position:absolute;left:193px;top:14px;font-size:12.5px;font-style:italic;color:var(--body-text)}
.news-arrows{position:absolute;right:14px;top:14px;display:flex;gap:12px}

.site-footer{position:absolute;left:120px;top:962px;width:880px;height:238px;background:var(--footer-grey);border-radius:6px 6px 0 0;overflow:hidden}
.site-footer>svg{position:absolute;left:0;top:0}
.footer-col{position:absolute;top:32px}
.footer-col h2{font-size:16px;color:var(--accent-teal);margin-bottom:14px}
.footer-links{list-style:none;width:190px}
.footer-links li{font-size:12.5px;color:var(--brand-navy);height:24.5px;line-height:24px;border-bottom:1px solid #b5b5b5;padding-left:16px;position:relative}
.footer-links li::before{content:"";position:absolute;left:0;top:7px;width:9px;height:9px;border-radius:50%;background:#eee;border:1px solid #999}
.social li{list-style:none;font-size:12.5px;color:var(--brand-navy);height:27px;display:flex;align-items:center;gap:12px}
.social .dot{width:18px;height:18px;background:#5b7fae;border-radius:2px}
.legal p{font-size:9.5px;line-height:17px;color:#777}
</style>
</head>
<body>

<header class="site-header">
  <div class="logo display">kVesta</div>
  <nav class="main-nav">
    <a href="#">HOME</a><a href="#">ABOUT US</a><a href="#">PROJECTS</a><a href="#">PORTFOLIOS</a><a href="#">TESTIMONIALS</a><a href="#">CONTACT</a>
  </nav>
</header>

<section class="hero">
  <div class="hero-photo"><div class="fill" role="img" aria-label="Photo of three business colleagues discussing work at a laptop"></div></div>
  <div class="hero-copy display">
    <div class="line">FOLLOW OUT SYSTEM</div>
    <div class="line">FOR GROWING YOUR</div>
    <div class="big">BUSINESS</div>
  </div>
  <div class="cta">Contact Us</div>
</section>

<h2 class="section-title display" style="left:123px;top:467px">ABOUT OUR COMPANY &nbsp;kVesta</h2>
<p class="about-text">I am an experienced builder in Crawley, Hollin Build have been based in Crawley for over 10 years. My team and I are proven, reliable builders based in Crawley. We've come across a lot in our time, so don't hesitate to get in touch about any building job in Crawley.</p>
<a class="more-link" href="#" style="left:125px;top:556px">LEARN MORE</a>

<h2 class="section-title display" style="left:123px;top:609px">kVesta FEATURED PROJECTS</h2>
<a class="more-link" href="#" style="left:568px;top:614px">VEIW PROJECTS</a>

<div class="projects">
  <div class="project"><div class="thumb"><div role="img" aria-label="Photo of a restored house interior with a dining table" style="background:linear-gradient(#8a8680,#2b2622 60%,#5a4e44)"></div></div><p>House Restoration in Crawley</p></div>
  <div class="project"><div class="thumb"><div role="img" aria-label="Photo of a converted loft room" style="background:linear-gradient(90deg,#d9cfc0,#a89683 50%,#e6ddcf)"></div></div><p>Loft Conversion Near Crawley</p></div>
  <div class="project"><div class="thumb"><div role="img" aria-label="Photo of a freshly painted living room with a sofa" style="background:linear-gradient(#e9dcc6,#c9a98a 55%,#8c3a2e)"></div></div><p>House Painting &amp; Decorating in Crawley</p></div>
  <div class="project"><div class="thumb"><div role="img" aria-label="Photo of a house extension with flowers" style="background:linear-gradient(135deg,#6c7a52,#c86a5e 50%,#e8dfd0)"></div></div><p>Beautiful House Extension in Crawley</p></div>
</div>

<aside class="testimonials">
  <h2 class="display">kVesta CLIENTS TESTIMONILAS</h2>
  <div class="testimonial"><h3>Mr. Varenko</h3><p>Hollin Build are the best builders in Crawley. They are experts in all areas of house building...</p></div>
  <div class="testimonial"><h3>Teodoro Valli</h3><p>I am Brazilian and I have website in Portuguese. Brightlane services are very good and I am very ha...</p></div>
  <div class="testimonial"><h3>Teodoro Valli</h3><p>I am Brazilian and I have website in Portuguese. Brightlane services are very good and I am very ha...</p></div>
  <a class="more-link" href="#" style="position:absolute;left:30px;top:378px">VEIW PROJECTS</a>
</aside>

<div class="news-bar">
  <div class="news-label display">LATEST NEWS
    <svg width="12" height="45" viewBox="0 0 12 45"><polygon points="0,0 12,22.5 0,45" fill="#1597be"/></svg>
  </div>
  <p class="news-text">Timber frames seem to be all the rage in London. Using the latest in wood tech!</p>
  <div class="news-arrows">
    <svg width="8" height="14" viewBox="0 0 8 14"><polyline points="7,1 1,7 7,13" fill="none" stroke="#111" stroke-width="2.5"/></svg>
    <svg width="8" height="14" viewBox="0 0 8 14"><polyline points="1,1 7,7 1,13" fill="none" stroke="#111" stroke-width="2.5"/></svg>
  </div>
</div>

<footer class="site-footer">
  <svg width="880" height="238" viewBox="0 0 880 238"><polygon points="262,0 550,0 597,119 550,238 280,238 310,119" fill="#f4f4f4"/></svg>
  <div class="footer-col" style="left:65px">
    <h2 class="display">kVesta</h2>
    <ul class="footer-links">
      <li>Home</li><li>About Us</li><li>Latest Projects</li><li>Latest News</li><li>Testimonials</li><li>Contacts Us</li>
    </ul>
  </div>
  <div class="footer-col" style="left:346px">
    <h2 class="display">SOCIAL SHARING</h2>
    <ul class="social">
      <li><span class="dot"></span>Become Fan on Linkora</li>
      <li><span class="dot"></span>Follow us on Chirply</li>
      <li><span class="dot"></span>Join us on Circlo</li>
      <li><span class="dot"></span>Email us on Netwerk</li>
    </ul>
  </div>
  <div class="footer-col legal" style="left:630px">
    <h2 class="display">LEGAL</h2>
    <p>All Rights Reserved. Copyright<br>2011 - © kVesta dot com<br>Privacy Policy &nbsp;| &nbsp;Terms of Use</p>
    <p style="margin-top:12px">Powered by Corvel Studio</p>
  </div>
</footer>

</body>
</html>
```